Coldforge Prime manufacturing Project

We are looking at getting a brand new design for a new company that deals in selling stainless tubing and other stainless still products such as handrails, Spigots, Balustrade Fittings
Glass, Glass fittings and Aluminium Channels

We require a very clean website that deals with the following colours:

Blue to light blues
Blacks
Greys to light Greys
Whites

We are open for other ideas BUT we *DO NOT* want any pinks, greens or bright colours except for backgrounds colours we have chosen above. (It can be solid, gradient or a subtle pattern)

YOU MUST KEEP THE LOGO AS IS. PLEASE DO NOT ALTER THE LOGO IN *ANY WAY* and the logo MUST be the same colours and fonts.

Logo is attached.

The site must contain these aspects:
jQuery Slider (Image slide show)
Top drop down Menus
Be no more than 900px wide
Text is to be to the w3C standards. (no special fonts)

We will chop up the design into html format. You just need to provide the PSD file.

The clients opposition is:
www.quorvatrim.example

Industry/Entity Type

It Company

Requirements
Nice to have
• Alter the logo in anyway

Files

```html
<!DOCTYPE html>
<html lang="en">
<head>
<meta charset="utf-8">
<title>Coldforge Prime – Stainless Products</title>
<link rel="stylesheet" href="https://fonts.googleapis.com/css2?family=Roboto:wght@300;400;500;700&family=Roboto+Condensed:wght@700&family=Roboto+Slab:wght@700&display=swap">
<style>
:root{
  --page:#f4f4f4;
  --white:#ffffff;
  --ink:#222222;
  --text:#6f6f6f;
  --muted:#8a8a8a;
  --blue:#1c5a9a;
  --blue-dark:#2b4a7a;
  --blue-hero:#3f7dbf;
  --blue-hero-light:#8ab6e0;
  --nav-top:#6d6d6d;
  --nav-bottom:#474747;
  --grey-card:#8d9ba2;
  --grey-line:#d8d8d8;
}
*{margin:0;padding:0;box-sizing:border-box}
html,body{width:1200px;height:1099px;overflow:hidden}
body{background:var(--page);font-family:"Roboto",sans-serif;color:var(--ink);position:relative}
.abs{position:absolute}

/* header */
.brand{left:226px;top:14px;width:125px;text-align:center}
.brand-mark{width:80px;height:80px;border-radius:50%;background:var(--blue-dark);margin:0 auto;border:6px solid #222}
.brand-name{font-size:15px;font-weight:400;color:#333;margin-top:6px;white-space:nowrap}
.brand-sub{font-size:7px;letter-spacing:1.5px;color:#555;white-space:nowrap}
.social{top:61px;left:487px;width:160px;display:flex;justify-content:space-between;font-size:11px;font-weight:700;color:var(--blue)}
.search{left:662px;top:55px;width:178px;height:27px;background:var(--white);border:1px solid #d4d4d4;font-size:12px;color:#999;padding:6px 0 0 24px}
.search svg.lens{position:absolute;left:7px;top:7px}
.search-btn{position:absolute;right:-1px;top:-1px;width:30px;height:27px;background:#555;display:flex;align-items:center;justify-content:center}
.help{left:852px;top:55px}
.help small{display:block;font-size:9px;color:#666}
.help strong{display:block;font-size:14px;font-weight:500;color:var(--blue);margin-top:1px}
.fittings-photo{left:833px;top:0;width:142px;height:40px;background:linear-gradient(90deg,#cfcfcf,#9a9a9a,#e0e0e0);border-radius:0 0 20px 20px}

.nav{left:414px;top:93px;width:560px;height:32px;background:linear-gradient(var(--nav-top),var(--nav-bottom));display:flex;align-items:center;padding-left:22px}
.nav a{color:var(--white);font-size:11.5px;font-weight:500;text-decoration:none;padding:0 11px;line-height:32px}
.nav a.active{background:var(--white);color:var(--blue);padding:0 14px}
.dropdown{left:537px;top:125px;width:193px;height:176px;background:var(--white);box-shadow:0 2px 4px rgba(0,0,0,.15);padding-top:10px;z-index:5}
.dropdown li{list-style:none;font-size:10.5px;color:#555;height:21.5px;line-height:21.5px;margin:0 8px;padding-left:12px}
.dropdown li.current{background:var(--blue-dark);color:var(--white);font-weight:500}

/* hero */
.hero{left:0;top:143px;width:1200px;height:356px;background:linear-gradient(100deg,#2f6eb0 0%,var(--blue-hero) 40%,var(--blue-hero-light) 100%);overflow:hidden}
.hero-photo{left:667px;top:0;width:341px;height:274px;background:linear-gradient(135deg,#5a6a7a,#e8ecef 45%,#7b8896 70%,#cfd6dc);opacity:.9}
.hero-title{left:225px;top:94px;color:var(--white);font-size:33px;font-weight:300;line-height:34px;white-space:nowrap}
.hero-title b{font-weight:700}
.hero-copy{left:226px;top:170px;width:380px;color:#eef4fb;font-size:13.5px;line-height:18.7px;font-weight:300}
.hero-btn{left:226px;top:244px;width:202px;height:29px;background:var(--white);font-family:"Roboto Slab",serif;font-size:12px;font-weight:700;color:var(--blue-dark);letter-spacing:.5px;padding:7px 0 0 16px}

/* content */
.section-title{font-size:14px;font-weight:500;color:var(--ink)}
.feature{width:272px;height:165px;background:linear-gradient(135deg,#7f8f97,#a9b5ba);border:1px solid #d0d0d0;color:var(--white)}
.feature h3{position:absolute;left:21px;top:23px;font-size:16px;font-weight:700}
.feature .spec{position:absolute;left:21px;top:43px;font-size:12px}
.feature p{position:absolute;left:20px;top:63px;width:120px;font-size:10.5px;line-height:13px;color:#e6ecef;font-weight:300}
.feature .view{position:absolute;left:20px;top:115px;width:112px;height:23px;background:var(--blue-dark);font-family:"Roboto Slab",serif;font-size:9.5px;letter-spacing:.6px;text-align:center;line-height:23px}
.feature .shot{position:absolute;left:141px;top:28px;width:125px;height:108px;background:linear-gradient(90deg,#d8dadb,#f5f5f5,#9ea3a6)}

.side-help{left:793px;top:539px;width:181px;height:113px;background:var(--white);border:1px solid #ddd}
.side-help .person{position:absolute;left:0;top:0;width:78px;height:112px;background:linear-gradient(#e9e3dd,#3a3a3a)}
.side-help h4{position:absolute;left:79px;top:31px;font-size:17px;color:var(--blue-dark);font-weight:700}
.side-help .chat{position:absolute;left:79px;top:54px;font-size:8px;color:#777}
.side-help .live{position:absolute;left:84px;top:75px;font-family:"Roboto Slab",serif;font-size:13.5px;color:#888}
.side-help .online{position:absolute;left:112px;top:96px;width:69px;height:16px;background:#4a7db5;color:var(--white);font-size:11px;font-weight:500;text-align:center;line-height:16px}
.side-cat{left:793px;top:664px;width:181px;height:198px;background:var(--white);border:1px solid #ddd;overflow:hidden}
.side-cat .lines{position:absolute;right:13px;top:14px;text-align:right;font-size:16px;font-weight:300;color:#444;line-height:19.5px;z-index:2}
.side-cat .lines b{font-weight:700;color:#222}
.side-cat .book{position:absolute;left:0;top:104px;width:181px;height:94px;background:linear-gradient(160deg,#3a3a3a 0%,#e6e6e6 35%,#cfcfcf 100%)}

.tile{width:178px;height:125px;background:var(--white);border:1px solid #ddd}
.tile .shot{height:98px;background:linear-gradient(#f7f7f7,#e2e2e2)}
.tile .label{height:26px;border-top:1px solid #e5e5e5;background:linear-gradient(#fafafa,#eee);font-family:"Roboto Condensed",sans-serif;font-size:12px;font-weight:700;color:#333;padding:7px 0 0 13px}

/* footer */
.footer{left:0;top:900px;width:1200px;height:199px;background:var(--white);border-top:2px solid #e3e3e3}
.footer-mark{left:226px;top:40px;width:60px;text-align:center}
.footer-mark .ring{width:44px;height:44px;border-radius:50%;background:#bfc4c8;border:3px solid #9a9a9a;margin:0 auto}
.footer-mark span{display:block;font-size:7px;color:#999;margin-top:3px;white-space:nowrap}
.footer h5{font-size:13.5px;font-weight:400;color:#333}
.footer p,.footer li{font-size:10.5px;line-height:16px;color:var(--muted);font-weight:300}
.col-about{left:305px;top:41px;width:240px}
.col-contact{left:583px;top:41px;width:135px}
.col-site{left:755px;top:41px;width:230px}
.col-about h5,.col-contact h5,.col-site h5{margin-bottom:7px}
.divider{top:35px;width:1px;height:116px;background:#e0e0e0}
.sitemap a{color:var(--muted);text-decoration:none;font-weight:400}
.sitemap a.on{color:var(--blue);font-weight:500}
.sitemap .sep{color:#bbb;margin:0 2px}
.copy{margin-top:7px;font-size:9.5px !important}
</style>
</head>
<body>

<header>
  <div class="abs brand">
    <div class="brand-mark"></div>
    <div class="brand-name">Coldforge Prime</div>
    <div class="brand-sub">Manufacturing Co. Ltd</div>
  </div>
  <div class="abs fittings-photo" role="img" aria-label="Chrome glass fittings"></div>
  <div class="abs social"><span>Flutter</span><span>Circlebook</span><span>StreamHub</span></div>
  <div class="abs search">
    <svg class="lens" width="11" height="11" viewBox="0 0 11 11"><circle cx="4.5" cy="4.5" r="3.5" fill="none" stroke="#aaa" stroke-width="1.3"/><line x1="7" y1="7" x2="10" y2="10" stroke="#aaa" stroke-width="1.3"/></svg>
    Search
    <span class="search-btn"><svg width="8" height="12" viewBox="0 0 8 12"><path d="M1 1l5 5-5 5" fill="none" stroke="#fff" stroke-width="2"/></svg></span>
  </div>
  <div class="abs help"><small>How May We Help?</small><strong>Call 800-555-0142</strong></div>
  <nav class="abs nav">
    <a href="#">HOME</a><a href="#">ABOUT</a><a class="active" href="#">PRODUCTS</a><a href="#">DOWNLOAD</a><a href="#">PRODUCTS</a><a href="#">DOWNLOAD</a><a href="#">CONTACT</a>
  </nav>
  <ul class="abs dropdown">
    <li>RailingSystem(42.4,33.7,48.3)</li>
    <li>RailingSystem(2´´,1.5´´,43)</li>
    <li class="current">Glass System</li>
    <li>Post &amp; Balustrade</li>
    <li>Accessories</li>
    <li>Square tube Fittings</li>
    <li>Sliding door &amp; Canopy</li>
  </ul>
</header>

<section class="abs hero">
  <div class="abs hero-photo" role="img" aria-label="Polished stainless steel tubes against the sky"></div>
  <h1 class="abs hero-title">The <b>Leading Manufacturer</b><br>in <b>Stainless</b> Products</h1>
  <p class="abs hero-copy">Innovative's glass component aluminum railing system are strong, aesthetically pleasing, and maintenance free. The transparent glass allows for a less obstructed view.</p>
  <div class="abs hero-btn">LEARN MORE ABOUT US ›</div>
</section>

<main>
  <h2 class="abs section-title" style="left:226px;top:518px">Featured Products</h2>
  <article class="abs feature" style="left:226px;top:539px">
    <h3>Railing System</h3><div class="spec">(42.4,33.7,48.3)</div>
    <p>Custom twisted in wire brushes, gun brushes, medical brushes,</p>
    <div class="view">VIEW PRODUCTS</div>
    <div class="shot" role="img" aria-label="Aluminium glass channel profile"></div>
  </article>
  <article class="abs feature" style="left:506px;top:539px">
    <h3>Railing System</h3><div class="spec">(42.4,33.7,48.3)</div>
    <p>Custom twisted in wire brushes, gun brushes, medical brushes,</p>
    <div class="view">VIEW PRODUCTS</div>
    <div class="shot" role="img" aria-label="Aluminium glass channel profile"></div>
  </article>

  <aside class="abs side-help">
    <div class="person" role="img" aria-label="Support agent with headset"></div>
    <h4>Need Help!</h4><div class="chat">CHAT ONLINE WITH US</div>
    <div class="live">Live Support</div><div class="online">ONLINE</div>
  </aside>
  <aside class="abs side-cat">
    <div class="lines">Download<br>Your Digital<br><b>Catalogue</b><br>Here!</div>
    <div class="book" role="img" aria-label="Open product catalogue"></div>
  </aside>

  <h2 class="abs section-title" style="left:227px;top:716px">All Products</h2>
  <div class="abs tile" style="left:226px;top:738px"><div class="shot" role="img" aria-label="Chrome elbow tube fitting"></div><div class="label">Bent, Pin&amp;Plate</div></div>
  <div class="abs tile" style="left:413px;top:738px"><div class="shot" role="img" aria-label="Stainless glass clamp"></div><div class="label">Glass Clamp 50.8mm</div></div>
  <div class="abs tile" style="left:600px;top:738px"><div class="shot" role="img" aria-label="Stainless glass holder"></div><div class="label">Glass Holder</div></div>
</main>

<footer class="abs footer">
  <div class="abs footer-mark"><div class="ring"></div><span>Coldforge Prime</span></div>
  <div class="abs col-about">
    <h5>About Coldforge Prime</h5>
    <p>Welcome to Coldforge Prime, your partner for professional railing, glass securing and glass channel systems. Find out more about new products and new ideas, our product range, quality and safety, functionality and design along side our philosophy, our company and the idea behind it.</p>
  </div>
  <div class="abs divider" style="left:557px"></div>
  <div class="abs col-contact">
    <h5>Contact Us</h5>
    <p>Coldforge Prime | Unit 12 - Harbor Works | Anvil Road | Eastmere | EM4 2QR | Tel.: +44 - 0800-5550199</p>
  </div>
  <div class="abs divider" style="left:731px"></div>
  <div class="abs col-site">
    <h5>Sitemap</h5>
    <p class="sitemap"><a class="on" href="#">Home</a><span class="sep">-</span><a href="#">About</a><span class="sep">-</span><a href="#">Products</a><span class="sep">-</span><a href="#">Download</a><span class="sep">-</span><a href="#">Contact</a><br><a href="#">Services</a><span class="sep">-</span><a href="#">Team</a><span class="sep">-</span><a href="#">Download</a><span class="sep">-</span><a href="#">Contact</a></p>
    <p class="copy">© 2008 Coldforge Prime Co. All Rights Reserved</p>
  </div>
</footer>

</body>
</html>
```